Clinical Research Consulting Company needs a web design

My consulting company provides service on clinical trial design and clincal research, product safety and claim development strategy, and lecture service.

Need template and graphic design for the website of my consulting company. Website will have many different tabs (e.g., Home, About Us, Service, and Contact Us).

Like to have modern look and easy on eyes (not too many colors).

We don't perform laboratory work so please do not use pictures with people working in the laboratory. Also, the logo is added. Thanks.

Target Market(s)

Pharmaceutical and Biotech companies, dietary supplement companies, food industry

Industry/Entity Type

It Company

Number of Pages Required

4 page

Font styles to use
Sans Serif

Requirements
Must have
• hyperlink to Contact Us page
Nice to have
• pictures

```html
<!DOCTYPE html>
<html lang="en">
<head>
<meta charset="utf-8">
<title>Corvana — Clinical Research Consulting</title>
<link href="https://fonts.googleapis.com/css2?family=Open+Sans:wght@400;600;700&display=swap" rel="stylesheet">
<style>
:root{
  --green:#3a9d48;
  --green-dark:#2f7f3b;
  --blue:#1f5c9c;
  --blue-deep:#154679;
  --blue-bar:#0f3560;
  --ink:#3b3b3b;
  --muted:#7a7a7a;
  --page:#f8f6f4;
  --card:#fdf3f0;
  --line:#e3dfdb;
  --white:#ffffff;
}
*{margin:0;padding:0;box-sizing:border-box}
html,body{width:876px;height:1200px;overflow:hidden}
body{font-family:'Open Sans',Arial,sans-serif;background:var(--page);color:var(--ink);position:relative;font-size:9px;line-height:1.45}
.hero{position:absolute;left:0;top:0;width:876px;height:308px;background:linear-gradient(180deg,#c9d3dc 0%,#aab7c3 45%,#8c8a86 100%)}
.hero-photo{position:absolute;inset:0;background:radial-gradient(ellipse at 30% 60%,#6b6f76 0%,transparent 55%),radial-gradient(ellipse at 80% 55%,#b9a79a 0%,transparent 50%),linear-gradient(180deg,#d6dde4,#9aa3ab 60%,#6c6a67)}
.brand{position:absolute;left:41px;top:0;width:86px;height:52px;background:var(--white);border-radius:0 0 6px 6px;display:flex;align-items:center;justify-content:center;gap:6px}
.brand-dot{width:12px;height:12px;border-radius:50%;background:var(--green)}
.brand-name{font-weight:700;font-size:12px;color:var(--blue)}
.nav{position:absolute;right:40px;top:48px;display:flex;gap:2px}
.nav a{display:block;padding:5px 12px;color:var(--white);font-size:9px;text-decoration:none;background:rgba(255,255,255,.18)}
.nav a.active{background:var(--green)}
.hero-title{position:absolute;top:240px;left:0;width:100%;text-align:center;color:var(--white);font-size:22px;font-weight:600;letter-spacing:1px;text-transform:uppercase}
.hero-sub{position:absolute;top:274px;left:0;width:100%;text-align:center;color:var(--white);font-size:15px}
.dots{position:absolute;top:322px;left:0;width:100%;display:flex;justify-content:center;gap:6px}
.dots span{width:7px;height:7px;border-radius:50%;background:#b9c6d3}
.dots span.on{background:var(--blue)}
.services{position:absolute;top:350px;left:41px;width:796px;display:flex;gap:12px}
.service{flex:1;background:var(--card);border:1px solid var(--line);padding:12px 12px 14px;height:160px}
.service-head{display:flex;align-items:center;gap:7px;margin-bottom:8px}
.icon{width:18px;height:18px;border-radius:50%;background:var(--green);flex:none}
.service h3{font-size:9px;color:var(--green-dark);text-transform:uppercase;font-weight:700}
.service p{color:var(--muted);font-size:8px;padding-left:25px}
.more{display:inline-block;margin:8px 0 0 25px;color:var(--blue);font-size:8px;font-weight:600}
.section-title{position:absolute;font-size:10px;font-weight:700;color:var(--ink)}
.blog{position:absolute;top:568px;left:41px;width:796px;display:flex;gap:12px}
.post{flex:1;text-align:center}
.thumb{height:64px}
.post h4{font-size:8px;color:var(--blue);margin-top:5px;font-weight:600}
.post small{font-size:7px;color:var(--muted)}
.news{position:absolute;top:700px;left:41px;width:420px}
.news-item{display:flex;gap:12px;margin-bottom:22px}
.news-thumb{width:100px;height:66px;flex:none}
.news-item h4{font-size:9px;color:var(--green-dark);font-weight:700}
.news-item .date{font-size:7px;color:var(--muted)}
.news-item p{font-size:8px;color:var(--muted);margin-top:3px}
.news-item .more{margin-left:0;margin-top:3px}
.find{position:absolute;top:700px;left:480px;width:357px}
.find-item{display:flex;gap:8px;margin-bottom:8px}
.find-item h5{font-size:8px;color:var(--green-dark);text-transform:uppercase;font-weight:700}
.find-item p{font-size:7.5px;color:var(--muted)}
.map{margin-left:26px;width:170px;height:98px}
.footer{position:absolute;top:922px;left:0;width:876px;height:248px;background:linear-gradient(180deg,var(--blue),var(--blue-deep))}
.foot-col{position:absolute;top:26px;width:240px;color:#d7e3f1;font-size:8px}
.foot-col h3{color:var(--white);font-size:10px;font-weight:700;text-transform:uppercase;margin-bottom:12px}
.update{display:flex;gap:8px;margin-bottom:14px}
.update .icon{background:#6f9fd1;width:14px;height:14px}
.update a{color:#9fc7ef}
.signup{display:flex;margin:10px 0 14px}
.signup span{flex:1;height:20px;background:var(--white);border-radius:2px 0 0 2px}
.signup b{background:var(--green);color:var(--white);padding:4px 10px;font-size:8px;border-radius:0 2px 2px 0}
.contact-line{display:flex;align-items:center;gap:8px;margin-bottom:7px}
.contact-line svg{flex:none}
.quote{font-style:italic}
.author{text-align:right;margin-top:6px;color:var(--white)}
.social{display:flex;gap:6px;margin-top:16px}
.social span{width:18px;height:18px;border-radius:50%;background:#6f9fd1}
.bottom-bar{position:absolute;top:1170px;left:0;width:876px;height:30px;background:var(--blue-bar);color:#c9d7e6;font-size:8px;padding:9px 41px}
</style>
</head>
<body>

<header class="hero">
  <div class="hero-photo" role="img" aria-label="Photo of consultants meeting around a conference table in a bright office"></div>
  <div class="brand"><span class="brand-dot"></span><span class="brand-name">Corvana</span></div>
  <nav class="nav">
    <a href="#" class="active">Home</a>
    <a href="#">About Us</a>
    <a href="#">Services</a>
    <a href="#">Blog</a>
    <a href="#">Contact Us</a>
  </nav>
  <h1 class="hero-title">Clinical Trial Design</h1>
  <p class="hero-sub">Reiciendis Voluptatibus Maiores</p>
</header>

<div class="dots"><span class="on"></span><span></span><span></span></div>

<section class="services">
  <article class="service">
    <div class="service-head"><span class="icon"></span><h3>Clinical Trial Design</h3></div>
    <p>We plan study protocols, endpoints and sample sizes so your trial answers the right question with clear, reliable evidence.</p>
    <a class="more">Learn More ›</a>
  </article>
  <article class="service">
    <div class="service-head"><span class="icon"></span><h3>Clinical Research</h3></div>
    <p>From site selection to final report, we guide research programs with careful oversight and practical, timely advice.</p>
    <a class="more">Learn More ›</a>
  </article>
  <article class="service">
    <div class="service-head"><span class="icon"></span><h3>Product Safety</h3></div>
    <p>Safety reviews and claim development strategy help products reach the market with confidence and sound supporting data.</p>
    <a class="more">Learn More ›</a>
  </article>
  <article class="service">
    <div class="service-head"><span class="icon"></span><h3>Lecture Service</h3></div>
    <p>Talks and workshops for teams who want a clear view of trial methods, regulation and research planning today.</p>
    <a class="more">Learn More ›</a>
  </article>
</section>

<h2 class="section-title" style="top:546px;left:41px">Latest from blog</h2>
<section class="blog">
  <div class="post"><div class="thumb" role="img" aria-label="Blog photo of a notebook on a desk" style="background:linear-gradient(135deg,#d9c8b4,#8f7c6a)"></div><h4>Study Endpoints</h4><small>by Author Name</small></div>
  <div class="post"><div class="thumb" role="img" aria-label="Blog photo of a team meeting" style="background:linear-gradient(135deg,#c7d3dd,#6d7d8c)"></div><h4>Protocol Reviews</h4><small>by Author Name</small></div>
  <div class="post"><div class="thumb" role="img" aria-label="Blog photo of a business discussion" style="background:linear-gradient(135deg,#d6dbe2,#4f6075)"></div><h4>Safety Reporting</h4><small>by Author Name</small></div>
  <div class="post"><div class="thumb" role="img" aria-label="Blog photo of fresh vegetables" style="background:linear-gradient(135deg,#c9b46a,#6f8a3c)"></div><h4>Nutrition Claims</h4><small>by Author Name</small></div>
</section>

<h2 class="section-title" style="top:676px;left:41px">Latest News</h2>
<section class="news">
  <article class="news-item">
    <div class="news-thumb" role="img" aria-label="News photo of a hand writing on paper" style="background:linear-gradient(135deg,#e2ddd6,#9a938a)"></div>
    <div>
      <h4>Temporibus lorem</h4>
      <span class="date">March 12, 2024</span>
      <p>New guidance on adaptive trial design was released this spring. We summarise what changes for sponsors and how to prepare study plans.</p>
      <a class="more">Learn More ›</a>
    </div>
  </article>
  <article class="news-item">
    <div class="news-thumb" role="img" aria-label="News photo of colleagues in an office" style="background:linear-gradient(135deg,#cfd8e0,#5d6e80)"></div>
    <div>
      <h4>Temporibus lorem</h4>
      <span class="date">February 26, 2024</span>
      <p>Our team joined a regional forum on supplement safety, sharing methods for building claims on sound clinical evidence and data.</p>
      <a class="more">Learn More ›</a>
    </div>
  </article>
</section>

<h2 class="section-title" style="top:676px;left:480px">Where to find us</h2>
<section class="find">
  <div class="find-item"><span class="icon"></span><div><h5>Official Webinar</h5><p>Monthly online session on trial planning, open to all clients.</p></div></div>
  <div class="find-item"><span class="icon"></span><div><h5>Voluptas Nulla</h5><p>Annual research meeting, booth 14, main exhibition hall.</p></div></div>
  <div class="map" role="img" aria-label="Map showing the office location" style="background:linear-gradient(135deg,#e8eef0,#c9d6da)"></div>
</section>

<footer class="footer">
  <div class="foot-col" style="left:41px">
    <h3>Latest Updates</h3>
    <div class="update"><span class="icon"></span><p>New article on study endpoints is live. Read it on our blog <a>#trials</a><br><small>2 hours ago</small></p></div>
    <div class="update"><span class="icon"></span><p>Join our next webinar on product safety and claim strategy <a>#research</a><br><small>1 day ago</small></p></div>
  </div>
  <div class="foot-col" style="left:320px">
    <h3>Newsletter</h3>
    <p>Subscribe to our email newsletter for useful tips and valuable resources.</p>
    <div class="signup"><span></span><b>Subscribe</b></div>
    <div class="contact-line">
      <svg width="12" height="9" viewBox="0 0 12 9"><rect x=".5" y=".5" width="11" height="8" fill="none" stroke="#d7e3f1"/><path d="M.5 .5 6 5l5.5-4.5" fill="none" stroke="#d7e3f1"/></svg>
      <span>hello@corvana-advisory.com</span>
    </div>
    <div class="contact-line">
      <svg width="12" height="12" viewBox="0 0 12 12"><path d="M3 1 5 3.5 4 5c.7 1.4 1.6 2.3 3 3l1.5-1L11 9l-1.5 2C5 10.5 1.5 7 1 2.5z" fill="#d7e3f1"/></svg>
      <span>+1 555 014 2290</span>
    </div>
    <div class="contact-line">
      <svg width="12" height="12" viewBox="0 0 12 12"><path d="M6 1a3.5 3.5 0 0 0-3.5 3.5C2.5 7 6 11 6 11s3.5-4 3.5-6.5A3.5 3.5 0 0 0 6 1z" fill="#d7e3f1"/></svg>
      <span>Request a meeting</span>
    </div>
  </div>
  <div class="foot-col" style="left:600px">
    <h3>Testimonials</h3>
    <p class="quote">“Their advice on our study design saved months of work. Clear, careful and always ready to explain each step.”</p>
    <p class="author">— Lena Marsh, R&amp;D Director</p>
    <div class="social"><span></span><span></span><span></span><span></span><span></span></div>
  </div>
</footer>

<div class="bottom-bar">© Copyright information here</div>

</body>
</html>
```